Pest Control Company needs business card!

Hi there, we need a business card designed for our new Pest Control Company. Ideally this card will be simple, yet feel elegant and high end. We want to use the colours Orange, Black and White. Please see our attached logo for the exact colours.

Business card details:

Phone - 0461 275 804
Name - Gavin Holloway
Email - Info@steadfastverminguard.com.au

We would also like to include the following list with dot points:

SERVICES / INSPECTIONS

Termites, Wood Borers, Ants, Cockroaches, Spiders, Fleas, Mice, Rats, Bed Bugs, & More!

```html
<!DOCTYPE html>
<html lang="en">
<head>
<meta charset="utf-8">
<title>Steadfast Vermin Guard – Business Card</title>
<link href="https://fonts.googleapis.com/css2?family=Roboto:wght@400;500;700;900&display=swap" rel="stylesheet">
<style>
  :root {
    --bg: #3b3532;
    --card: #262626;
    --card-back: #222222;
    --orange: #f7931e;
    --red: #e8262b;
    --white: #ffffff;
  }
  * { margin: 0; padding: 0; box-sizing: border-box; }
  html, body { width: 1200px; height: 716px; overflow: hidden; }
  body {
    background: var(--bg);
    font-family: "Roboto", sans-serif;
    position: relative;
  }
  .card {
    position: absolute;
    width: 540px;
    height: 309px;
    top: 204px;
    box-shadow: 0 6px 18px rgba(0,0,0,.35);
  }
  .card--back { left: 40px; background: var(--card-back); }
  .card--front { left: 620px; background: var(--card); color: var(--white); }

  .brand {
    position: absolute;
    color: var(--orange);
    font-weight: 900;
    text-transform: uppercase;
    line-height: 1;
    display: flex;
    align-items: center;
    gap: 10px;
  }
  .brand__dot {
    width: 16px; height: 16px; border-radius: 50%;
    background: var(--orange); flex: none;
  }
  .card--back .brand {
    left: 0; right: 0; top: 0; bottom: 0;
    justify-content: center;
    font-size: 22px;
  }
  .card--front .brand {
    left: 36px; top: 78px; width: 230px;
    font-size: 24px;
    align-items: flex-start;
  }
  .card--front .brand__dot { margin-top: 4px; }

  .divider {
    position: absolute;
    left: 282px; top: 70px;
    width: 1.5px; height: 126px;
    background: var(--orange);
  }
  .person { position: absolute; left: 296px; top: 74px; }
  .person__name {
    color: var(--orange); font-weight: 700; font-size: 18px;
    text-transform: uppercase; letter-spacing: .3px;
  }
  .person__role { font-size: 12px; margin-top: 2px; }

  .contacts {
    position: absolute; left: 296px; top: 130px;
    list-style: none; font-size: 12px;
  }
  .contacts li { display: flex; align-items: center; gap: 6px; height: 19px; }
  .contacts svg { width: 10px; height: 10px; flex: none; }

  .services {
    position: absolute; left: 38px; top: 226px;
    font-size: 12.5px; text-transform: uppercase; line-height: 21px;
  }
  .services .sep { color: var(--orange); margin: 0 5px; }
</style>
</head>
<body>
  <section class="card card--back" aria-label="Card back">
    <div class="brand"><span class="brand__dot"></span>Steadfast Vermin Guard</div>
  </section>

  <section class="card card--front" aria-label="Card front">
    <div class="brand"><span class="brand__dot"></span><span>Steadfast Vermin Guard</span></div>
    <div class="divider"></div>
    <div class="person">
      <div class="person__name">Gavin Holloway</div>
      <div class="person__role">President</div>
    </div>
    <ul class="contacts">
      <li>
        <svg viewBox="0 0 10 10"><path d="M2 0.5 L4 2.8 L3 4 Q4 6 6 7 L7.2 6 L9.5 8 L8 9.6 Q3.5 9.5 0.4 2 Z" fill="var(--red)"/></svg>
        0461 275 804
      </li>
      <li>
        <svg viewBox="0 0 10 10"><rect x="0.5" y="2" width="9" height="6.5" fill="var(--red)"/><path d="M0.5 2 L5 5.5 L9.5 2" stroke="var(--card)" stroke-width="0.9" fill="none"/></svg>
        Info@steadfastverminguard.com.au
      </li>
      <li>
        <svg viewBox="0 0 10 10"><circle cx="5" cy="5" r="4.5" fill="var(--red)"/><path d="M5 0.5 V9.5 M0.5 5 H9.5" stroke="var(--card)" stroke-width="0.8"/></svg>
        www.steadfastverminguard.com.au
      </li>
    </ul>
    <div class="services">
      <div>Termites<span class="sep">•</span>Wood Borers<span class="sep">•</span>Ants<span class="sep">•</span>Cockroaches</div>
      <div>Spiders<span class="sep">•</span>Fleas<span class="sep">•</span>Mice<span class="sep">•</span>Rats<span class="sep">•</span>Bed Bugs<span class="sep">•</span>&amp; More!</div>
    </div>
  </section>
</body>
</html>
```